Pediatric Therapy Clinic Brochure

We need a Brochure for a new pediatric therapy clinic. The clinic offers occupational therapy, physical therapy, speech therapy and feeding therapy. We want a brochure for parents, doctors and medical professional. It should have a fun and inviting, but still professional feel. Should be kid focused, bright and colorful. All the text / wording is there and a rough layout. Now I need someone to tidy and jazz it up and make it look professional.

Target Market(s)

Parents, doctors, medical professional

Industry/Entity Type

Medical

Font styles to use
Serif
Sans Serif

Requirements
Must have
• Keep All the text with information about services the same. Logo on front. Pictures throughout (use any of the pictures provided) (try and match up with corresponding service) (pictures are labeled). Need to have Map and contact info
• Keep colors consistent with our logo
Nice to have
• Background, special effects. Make it look fancy and professional
Should not have
• Not so busy that is takes away from the text

```html
<!DOCTYPE html>
<html lang="en">
<head>
<meta charset="utf-8">
<title>Pediatric Therapy Services Brochure</title>
<link rel="stylesheet" href="https://fonts.googleapis.com/css2?family=Marcellus&family=Lato:wght@700&display=swap">
<style>
  :root {
    --brand-blue: #1f5fa3;
    --band-blue: #4f86bf;
    --band-orange: #f08a5c;
    --accent-orange: #f2652a;
    --paper: #ffffff;
  }
  * { box-sizing: border-box; margin: 0; padding: 0; }
  html, body { width: 1200px; height: 863px; overflow: hidden; background: var(--paper); }
  .brochure { position: relative; width: 1200px; height: 863px; background: var(--paper); font-family: "Lato", Arial, sans-serif; }

  .photo { position: absolute; }
  .photo-painted-hands { left: 140px; top: 190px; width: 114px; height: 130px; border-radius: 50% 50% 8px 8px; background: radial-gradient(circle at 50% 45%, #f5d9c4 0%, #e9c7b0 45%, #f7f2ee 100%); }
  .photo-friends { left: 96px; top: 540px; width: 212px; height: 140px; border-radius: 6px; background: radial-gradient(ellipse at 50% 50%, #e9c3ad 0%, #e8a9b4 45%, #f6f1ee 100%); box-shadow: 3px 3px 6px rgba(0,0,0,.15); }
  .photo-faint { opacity: .22; border-radius: 50%; background: radial-gradient(circle, #e4c09a 0%, #f0e0cf 55%, rgba(255,255,255,0) 75%); }
  .faint-speech { left: 520px; top: 240px; width: 120px; height: 140px; }
  .faint-feeding { left: 920px; top: 245px; width: 110px; height: 110px; }
  .faint-physical { left: 960px; top: 440px; width: 140px; height: 140px; background: radial-gradient(circle, #e85d9a 0%, #f3b9d0 50%, rgba(255,255,255,0) 75%); }

  .bands { position: absolute; left: 0; top: 662px; width: 1200px; height: 60px; }

  .arch { position: absolute; left: 654px; top: 454px; width: 214px; height: 268px; }

  .banner { position: absolute; width: 254px; background: var(--brand-blue); color: #fff; text-align: center; clip-path: polygon(0 0, 100% 0, 100% 84%, 50% 100%, 0 84%); }
  .banner-title { font-family: "Marcellus", Georgia, serif; font-size: 16.5px; letter-spacing: .3px; line-height: 1; }
  .banner-text { font-family: "Lato", Arial, sans-serif; font-size: 7.4px; line-height: 10px; text-transform: uppercase; margin-top: 3px; }

  .banner-occupational { left: 69px; top: 320px; height: 76px; padding: 13px 14px 0; }
  .banner-speech { left: 469px; top: 180px; height: 54px; padding: 15px 20px 0; }
  .banner-sensory { left: 469px; top: 398px; height: 76px; padding: 6px 10px 0; }
  .banner-feeding { left: 878px; top: 180px; height: 70px; padding: 15px 20px 0; }
  .banner-physical { left: 878px; top: 356px; height: 58px; padding: 5px 14px 0; }
  .banner-group { left: 878px; top: 566px; height: 58px; padding: 5px 20px 0; }

  .service-list { position: absolute; list-style: none; color: var(--accent-orange); font-size: 9.4px; line-height: 12px; text-transform: uppercase; letter-spacing: .15px; }
  .service-list li { position: relative; padding-left: 22px; margin-bottom: 1.5px; }
  .service-list li::before { content: ""; position: absolute; left: 0; top: 4px; width: 3.5px; height: 3.5px; border-radius: 50%; background: var(--accent-orange); }
  .service-list li.note::before { display: none; }
  .list-occupational { left: 48px; top: 399px; width: 260px; }
  .list-speech { left: 447px; top: 250px; width: 250px; }
  .list-sensory { left: 447px; top: 480px; width: 250px; }
  .list-feeding { left: 854px; top: 254px; width: 250px; }
  .list-physical { left: 854px; top: 410px; width: 240px; }
  .list-group { left: 853px; top: 620px; width: 250px; }
  .list-physical li, .list-feeding li { margin-bottom: 2.3px; }
</style>
</head>
<body>
<main class="brochure">
  <div class="photo photo-faint faint-speech" role="img" aria-label="Faded photo of a smiling toddler"></div>
  <div class="photo photo-faint faint-feeding" role="img" aria-label="Faded photo of a baby eating"></div>
  <div class="photo photo-faint faint-physical" role="img" aria-label="Faded photo of a child on an exercise ball"></div>

  <svg class="bands" viewBox="0 0 1200 60" aria-hidden="true">
    <path d="M0 0 H70 L86 16 H330 L346 0 H1200 V32 H0 Z" fill="var(--band-blue)"/>
    <rect x="0" y="32" width="1200" height="28" fill="var(--band-orange)"/>
  </svg>

  <svg class="arch" viewBox="0 0 214 268" role="img" aria-label="Photo of a laughing toddler playing on a therapy ball, framed in an arch">
    <defs>
      <radialGradient id="archFill" cx="50%" cy="55%" r="65%">
        <stop offset="0%" stop-color="#e9c5a8"/>
        <stop offset="45%" stop-color="#d75a4e"/>
        <stop offset="100%" stop-color="#cfd6e6"/>
      </radialGradient>
    </defs>
    <path d="M22 268 V110 A85 85 0 0 1 192 110 V268 Z" fill="url(#archFill)" opacity=".85"/>
    <path d="M6 268 V110 A101 101 0 0 1 208 110 V268 H192 V110 A85 85 0 0 0 22 110 V268 Z" fill="var(--band-blue)"/>
    <line x1="143" y1="20" x2="143" y2="268" stroke="#fff" stroke-width="1"/>
  </svg>

  <div class="photo photo-painted-hands" role="img" aria-label="Photo of a girl showing paint-covered hands"></div>
  <div class="photo photo-friends" role="img" aria-label="Photo of three children whispering and laughing together"></div>

  <section>
    <header class="banner banner-occupational">
      <h2 class="banner-title">OCCUPATIONAL THERAPY</h2>
      <p class="banner-text">Helping children build better self-esteem, confidence and independence in all the things they do.</p>
    </header>
    <ul class="service-list list-occupational">
      <li>Sensory processing disorder</li>
      <li>Balance, coordination, strength, and endurance</li>
      <li>Fine motor and handwriting</li>
      <li>Visual- motor integration</li>
      <li>Play and social skills</li>
      <li>Feeding and oral motor skills</li>
      <li>Self-care</li>
      <li>Academic and cognitive skills</li>
      <li>Behavioral difficulties</li>
      <li>Developmental delays</li>
    </ul>
  </section>

  <section>
    <header class="banner banner-speech">
      <h2 class="banner-title">SPEECH THERAPY</h2>
      <p class="banner-text">Helping children speak, communicate and understand language.</p>
    </header>
    <ul class="service-list list-speech">
      <li>Expressive and receptive language</li>
      <li>Speech and language developmental milestones</li>
      <li>Articulation / intelligibility</li>
      <li>Speech fluency–</li>
      <li>Pragmatics and social skills</li>
      <li>Literacy and vocabulary</li>
      <li>Apraxia of speech</li>
      <li>Augmentative and alternative communication</li>
      <li>Feeding and oral motor</li>
    </ul>
  </section>

  <section>
    <header class="banner banner-sensory">
      <h2 class="banner-title">SENSORY INTEGRATION</h2>
      <p class="banner-text">Gradually increasing play based activities to improve a child's nervous system. Helping children learn to self-regulate their emotions, behaviors and arousal levels.</p>
    </header>
    <ul class="service-list list-sensory">
      <li>Autism and ADHD</li>
      <li>Sensory processing disorder</li>
      <li>Poor tolerance of sensory stimuli from the environment</li>
      <li>Meltdowns and tantrums</li>
      <li>Poor balance/body awareness</li>
      <li>Poor attention and concentration</li>
      <li>Poor self-regulation</li>
      <li>Behavior and social difficulties</li>
      <li>Poor motor coordination and motor planning</li>
      <li>Aggression, frustration or avoidance behaviors</li>
    </ul>
  </section>

  <section>
    <header class="banner banner-feeding">
      <h2 class="banner-title">FEEDING THERAPY</h2>
      <p class="banner-text">Providing skilled assessment and intervention to children with feeding difficulties.</p>
    </header>
    <ul class="service-list list-feeding">
      <li>Food aversions</li>
      <li>Food refusal</li>
      <li>Very picky eating</li>
      <li>Avoidance of certain textures</li>
      <li>Gagging and vomiting</li>
      <li>Oral motor/ chewing difficulties</li>
      <li>Limited diet/food repertoire</li>
    </ul>
  </section>

  <section>
    <header class="banner banner-physical">
      <h2 class="banner-title">PHYSICAL THERAPY</h2>
      <p class="banner-text">Helping children move and interact within their environment smoothly and confidently.</p>
    </header>
    <ul class="service-list list-physical">
      <li>Torticollis</li>
      <li>Walking and mobility</li>
      <li>Developmental motor milestones</li>
      <li>Balance, coordination, motor planning</li>
      <li>Strength, muscle tone and range of motion</li>
      <li>Toe walking</li>
      <li>Sports injuries</li>
      <li>Myofascial release</li>
      <li>Postural control and positioning</li>
    </ul>
  </section>

  <section>
    <header class="banner banner-group">
      <h2 class="banner-title">GROUP THERAPY</h2>
      <p class="banner-text">Using peer role models to learn new and challenging skills.</p>
    </header>
    <ul class="service-list list-group">
      <li>Social groups</li>
      <li>Feeding groups</li>
      <li class="note">**More group classes coming soon</li>
    </ul>
  </section>
</main>
</body>
</html>
```